Brighten-The-Room - DL Flyer - Kitchen Renovations & Cabinetry - Eye Catching Design

Please design a creative, professional DL flyer for us (DL Size: 98 x 210mmm), incorporating details outlined below...

Font: Helvetica Neue (same as logo)

Front: Main logo (01.eps) as a feature, website on the bottom (brighten-the-room.com.au).

Back: Three key words to be featured: Kitchens I Benchtops I Custom Cabinetry
2-3 clear images showing our work (more have been provided so you can select the images that work the best with the design). We have also attached the icon from our logo on 4 x different colour backgrounds, which could be incorporated (on back).
Text to include: 'Servicing all areas, we come to you!'

Contact details: 'Call us now on 0417 268 391'. enquiries@brighten-the-room.com.au Lic. No. BLD 738402

Look forward to seeing what you come up with.

Target Market(s)

Home owners, 35-80+ age bracket

Industry/Entity Type

Kitchen

Font styles to use
Other font styles liked:
• Helvetica Neue

Requirements
Must have
• Logo and website on front page of flyer. Minimum of 2-3 images incorporated. Contact details as per project description. Text on back page, 3 key words: Kitchens I Benchtops I Custom Cabinetry
• Creative, eye-catching design layout. Consistent theming with business card (see attached), including colours (grey, white, blues)
Nice to have
• Creative, eye-catching way to incorporate photos.
Should not have
• Not too busy/cluttered

```html
<!DOCTYPE html>
<html lang="en">
<head>
<meta charset="utf-8">
<title>Brighten-The-Room – DL Flyer</title>
<link rel="stylesheet" href="https://fonts.googleapis.com/css2?family=Roboto+Condensed:wght@700&family=Lato:ital,wght@0,700;1,400;1,700&family=Questrial&display=swap">
<style>
  :root {
    --blue: #4a72c0;
    --blue-deep: #3c62ae;
    --charcoal: #4a4a4c;
    --grey-text: #5a5a5c;
    --paper: #ffffff;
    --paper-shade: #e4e5e8;
    --backdrop: #ecebe8;
    --photo-warm-1: #f3e6b2;
    --photo-warm-2: #c9b27a;
    --photo-warm-3: #6d6246;
  }
  * { margin: 0; padding: 0; box-sizing: border-box; }
  html, body { width: 1200px; height: 825px; overflow: hidden; }
  body { background: var(--backdrop); position: relative; }

  .flyer {
    position: absolute; top: 82px; width: 324px; height: 688px;
    background: linear-gradient(180deg, var(--paper) 0%, var(--paper) 55%, var(--paper-shade) 100%);
    box-shadow: 0 6px 18px rgba(0,0,0,.18);
    overflow: hidden;
  }
  .flyer--front { left: 224px; }
  .flyer--back { left: 638px; }

  .brand {
    position: absolute; top: 38px; left: 0; width: 100%;
    display: flex; justify-content: center; align-items: center; gap: 8px;
    font: 700 20px/1 "Lato", sans-serif; color: var(--charcoal); letter-spacing: .5px;
  }
  .brand__mark { width: 14px; height: 14px; background: var(--blue); }

  .chevron-art { position: absolute; left: 0; top: 0; }

  .headline {
    position: absolute; left: 0; width: 100%; text-align: center;
    font-family: "Roboto Condensed", sans-serif; font-weight: 700; color: var(--blue);
  }
  .headline--main { top: 360px; font-size: 34px; line-height: 1; }
  .headline--sub { top: 400px; font-size: 19px; line-height: 1; }

  .call-bar {
    position: absolute; top: 446px; left: 0; width: 100%; height: 42px;
    background: var(--charcoal); border-top: 2px solid var(--blue);
    color: #fff; text-align: center;
    font: 700 22px/40px "Roboto Condensed", sans-serif;
  }

  .work-photos { position: absolute; left: 0; width: 100%; display: flex; justify-content: center; gap: 12px; }
  .flyer--front .work-photos { top: 516px; }
  .flyer--back .work-photos { top: 394px; }
  .work-photo {
    width: 90px; height: 90px; border-radius: 50%;
    border: 5px solid var(--blue); box-shadow: 0 4px 8px rgba(0,0,0,.2);
  }
  .work-photo--benchtop { background: radial-gradient(circle at 40% 40%, #f4f3ee, #c9ccc8 70%, #8f9a96); }
  .work-photo--drawer { background: radial-gradient(circle at 50% 45%, #f6f4ec, #d7cfbd 60%, #8c7a5e); }
  .work-photo--steel { background: radial-gradient(circle at 45% 40%, #dfe2e4, #a8adb1 60%, #55595e); }
  .work-photo--gloss { background: radial-gradient(circle at 45% 45%, #d8c69a, #3a2a20 65%, #1f1712); }
  .work-photo--shelving { background: linear-gradient(135deg, #5c2a1e, #2a1410 50%, #8a6a58); }
  .work-photo--bathroom { background: radial-gradient(circle at 50% 50%, #f3e6de, #e0c6bb 60%, #c9a89a); }

  .divider { position: absolute; top: 630px; left: 0; width: 100%; height: 6px; background: var(--charcoal); }
  .footer {
    position: absolute; top: 636px; left: 0; width: 100%; height: 52px;
    background: var(--blue); border-top: 2px solid #fff;
    color: #fff; text-align: center;
    font: 16px/50px "Questrial", sans-serif; letter-spacing: .3px;
  }

  .section-title {
    position: absolute; top: 30px; left: 0; width: 100%; text-align: center;
    font: 700 20px/1 "Roboto Condensed", sans-serif; color: var(--blue);
  }
  .copy {
    position: absolute; left: 26px; width: 272px; text-align: center;
    font: italic 400 11.2px/13.6px "Lato", sans-serif; color: var(--grey-text);
  }
  .copy--intro { top: 60px; }
  .copy--services { top: 500px; }

  .service-area {
    position: absolute; top: 598px; left: 0; width: 100%; text-align: center;
    font: italic 700 11.5px/1 "Lato", sans-serif; color: var(--blue);
  }
  .contact-line {
    position: absolute; top: 613px; left: 0; width: 100%; text-align: center;
    font: italic 400 10px/1 "Lato", sans-serif; color: var(--grey-text);
  }

  .keyword-bar {
    position: absolute; top: 338px; left: 0; width: 100%; height: 42px;
    background: var(--blue-deep); color: #fff; text-align: center;
    font: 700 17px/42px "Roboto Condensed", sans-serif;
  }
</style>
</head>
<body>

<section class="flyer flyer--front">
  <div class="brand"><span class="brand__mark"></span>BRIGHTEN-THE-ROOM</div>

  <svg class="chevron-art" width="324" height="360" viewBox="0 0 324 360">
    <defs>
      <linearGradient id="studyRoomTones" x1="0" y1="0" x2="1" y2="1">
        <stop offset="0" stop-color="var(--photo-warm-1)"/>
        <stop offset=".55" stop-color="var(--photo-warm-2)"/>
        <stop offset="1" stop-color="var(--photo-warm-3)"/>
      </linearGradient>
    </defs>
    <polygon points="0,118 162,80 324,118 324,130 162,92 0,130" fill="var(--blue)"/>
    <polygon role="img" aria-label="Photo of a built-in study nook with desks, overhead cabinets and two white chairs"
      points="0,134 162,96 324,134 324,292 162,318 0,292" fill="url(#studyRoomTones)"/>
    <polygon points="0,305 162,330 324,305 324,318 162,343 0,318" fill="var(--blue)"/>
  </svg>

  <h1 class="headline headline--main">Enquire how we can</h1>
  <p class="headline headline--sub">Brighten-The-Room in your home!</p>

  <div class="call-bar">Call us today on 0417 268 391</div>

  <div class="work-photos">
    <div class="work-photo work-photo--benchtop" role="img" aria-label="Photo of a white kitchen benchtop with cabinetry"></div>
    <div class="work-photo work-photo--drawer" role="img" aria-label="Photo of an open kitchen drawer with tea towels"></div>
    <div class="work-photo work-photo--steel" role="img" aria-label="Photo of a stainless steel benchtop and sink"></div>
  </div>

  <div class="divider"></div>
  <footer class="footer">www.brighten-the-room.com.au</footer>
</section>

<section class="flyer flyer--back">
  <h2 class="section-title">WHAT WE OFFER</h2>
  <p class="copy copy--intro">At Brighten-The-Room, we take pride in transforming areas of your home with innovative &amp; functional cabinetry solutions, uniquely crafted to suit your requirements. Based in the Adelaide Hills, we offer our services throughout Adelaide and surrounds.</p>

  <svg class="chevron-art" width="324" height="340" viewBox="0 0 324 340">
    <defs>
      <linearGradient id="studyRoomTonesBack" x1="0" y1="0" x2="1" y2="1">
        <stop offset="0" stop-color="var(--photo-warm-1)"/>
        <stop offset=".55" stop-color="var(--photo-warm-2)"/>
        <stop offset="1" stop-color="var(--photo-warm-3)"/>
      </linearGradient>
    </defs>
    <polygon points="0,180 162,150 324,180 324,192 162,162 0,192" fill="var(--blue)"/>
    <polygon role="img" aria-label="Photo of a built-in study nook with desks, shelving and office chairs"
      points="0,196 162,166 324,196 324,338 0,338" fill="url(#studyRoomTonesBack)"/>
  </svg>

  <div class="keyword-bar">Kitchens I Benchtops I Custom Cabinetry</div>

  <div class="work-photos">
    <div class="work-photo work-photo--gloss" role="img" aria-label="Photo of a glossy cabinet edge with lighting"></div>
    <div class="work-photo work-photo--shelving" role="img" aria-label="Photo of dark timber shelving"></div>
    <div class="work-photo work-photo--bathroom" role="img" aria-label="Photo of a bathroom vanity with towels"></div>
  </div>

  <p class="copy copy--services">We can design, supply &amp; install new custom cabinetry for your kitchen, bathroom, laundry, entertainment areas, living spaces, bedroom wardrobes, study rooms &amp; more. Transforming a dormant space into a functional and aesthetically pleasing part of your home, can be as simple as incorporating well designed &amp; carefully thought out cabinetry.</p>

  <p class="service-area">Servicing all areas, we come to you!</p>
  <p class="contact-line">enquiries@brighten-the-room.com.au &nbsp;|&nbsp; Lic. No. BLD 738402</p>

  <div class="divider"></div>
  <footer class="footer">www.brighten-the-room.com.au</footer>
</section>

</body>
</html>
```